Chatterly Brillaria4 to attract customers

We need a Chatterly design that brings seriousness and professionalism in the field of business advice. We enclose the logo that a colleague of yours designed in Artquarry.
The company is called: Brillaria4 Asesoría y Administración de Empresas, but the commercial name is Brillaria4.
We are dedicated to advising companies, providing the following services: tax, labor, accounting, administration and finance.
We would like a design that respects the colors of the attached logo, we also attach the logo in black and white, in case you need it for an image. The design, as we have already said, must communicate security, trust, professionalism and also be attractive for sale, that is, that customers who visit Chatterly are attracted to ask for information, call, or give "like" in the page.
The client profile we are looking for are companies and freelancers.

Target Market(s)

Companies and freelancers in Spain

Industry/Entity Type

Asesoría de empresas, Consultoría

Font styles to use
Sans Serif

Colors
0054AA
0677BA
7BADD7
CADEEF
E8F1F8

Requirements
Must have
• We are a business consultancy so it must convey seriousness, professionalism, trust and that encourages being sold, that is, those who agree contact us or like the page
Nice to have
• Create a cover photo, that the services appear (Tax, Labor, Accounting, Administration and Financial), profile image (we have attached the logo if it is worth it), contact forms and access to quick likes. It is very important that it is compatible with the SEO and SEM of the company. We also seek to design a kind of "template" for our publications, making sure that each time we publish a format and an image are followed and we are recognized just by seeing the publication

```html
<!DOCTYPE html>
<html lang="es">
<head>
<meta charset="utf-8">
<title>Brillaria4 – Portada</title>
<link rel="stylesheet" href="https://fonts.googleapis.com/css2?family=Nunito:wght@600;700;800;900&display=swap">
<style>
  :root {
    --page-bg: #eef1f4;
    --navy: #0b1f7c;
    --royal: #0054aa;
    --brand-blue: #0677ba;
    --sky: #1ba4e2;
    --soft: #7badd7;
    --pale: #cadeef;
    --mist: #e8f1f8;
    --ink: #1b3a9c;
    --grey-text: #7a7f88;
    --white: #ffffff;
  }
  * { margin: 0; padding: 0; box-sizing: border-box; }
  html, body {
    width: 1200px; height: 1022px; overflow: hidden;
    background: var(--page-bg);
    font-family: "Nunito", sans-serif;
  }
  .cover {
    position: absolute; left: 20px; top: 296px;
    width: 1160px; height: 430px; overflow: hidden;
    background: linear-gradient(180deg, #f7f8fa 0%, #eceff2 100%);
  }
  .cover-shapes, .cover-photo {
    position: absolute; inset: 0; width: 1160px; height: 430px;
  }
  .brand {
    position: absolute; left: 50px; top: 34px;
    display: flex; align-items: flex-start; gap: 12px;
  }
  .brand-mark {
    width: 56px; height: 56px; margin-top: 8px;
    background: var(--royal);
  }
  .brand-name {
    font-weight: 800; font-size: 34px; line-height: 1;
    color: var(--royal); letter-spacing: 0.5px; margin-top: 10px;
  }
  .brand-tagline {
    font-weight: 600; font-size: 13.5px; line-height: 1.3;
    color: var(--grey-text); letter-spacing: 1px; margin-top: 6px;
    text-transform: uppercase;
  }
  .services-title {
    position: absolute; left: 50px; top: 157px;
    width: 362px; height: 33px;
    border-bottom: 2px solid var(--royal);
  }
  .services-title span {
    display: inline-block; height: 31px; padding: 0 34px 0 12px;
    background: var(--royal); color: var(--white);
    font-weight: 900; font-size: 20px; letter-spacing: 1.5px; line-height: 31px;
    clip-path: polygon(0 0, 86% 0, 100% 100%, 0 100%);
  }
  .service {
    position: absolute; display: flex; align-items: center; gap: 10px;
    color: var(--ink); font-weight: 800; font-size: 22px;
  }
  .service svg { width: 26px; height: 26px; fill: none; stroke: #6b7280; stroke-width: 1.6; }
  .contact-band {
    position: absolute; left: 0; top: 347px; height: 83px; width: 620px;
    color: var(--white);
  }
  .contact-call { position: absolute; left: 46px; top: 14px; }
  .call-label { font-weight: 800; font-size: 14.5px; }
  .call-number {
    display: flex; align-items: center; gap: 6px;
    font-weight: 900; font-size: 34px; line-height: 1.1;
  }
  .call-number svg { width: 24px; height: 24px; fill: var(--white); }
  .contact-divider {
    position: absolute; left: 278px; top: 16px; width: 2px; height: 54px;
    background: var(--white);
  }
  .contact-online { position: absolute; left: 296px; top: 12px; }
  .contact-line {
    display: flex; align-items: center; gap: 8px;
    font-weight: 700; font-size: 23px; line-height: 29px;
  }
  .contact-line svg { width: 17px; height: 17px; fill: none; stroke: var(--white); stroke-width: 1.8; }
</style>
</head>
<body>
  <section class="cover">
    <svg class="cover-shapes" viewBox="0 0 1564 580" preserveAspectRatio="none" aria-hidden="true">
      <defs>
        <linearGradient id="bandFill" x1="0" y1="0" x2="1" y2="0">
          <stop offset="0" stop-color="#0a6fc4"/>
          <stop offset="1" stop-color="#1b9fe0"/>
        </linearGradient>
      </defs>
      <polygon points="0,468 742,468 812,580 0,580" fill="url(#bandFill)"/>
      <polygon points="860,0 895,0 735,297 895,580 845,580 650,297" fill="var(--sky)"/>
      <polygon points="890,0 988,0 825,297 988,580 890,580 730,297" fill="var(--navy)"/>
    </svg>
    <svg class="cover-photo" viewBox="0 0 1564 580" preserveAspectRatio="none" role="img" aria-label="Foto de una persona trabajando en un portátil con gráficos financieros sobre un escritorio">
      <defs>
        <linearGradient id="photoFill" x1="0" y1="0" x2="1" y2="1">
          <stop offset="0" stop-color="#e6e7e4"/>
          <stop offset="0.55" stop-color="#cfcfcb"/>
          <stop offset="1" stop-color="#d9c9a8"/>
        </linearGradient>
      </defs>
      <polygon points="1000,0 1564,0 1564,580 1000,580 838,297" fill="url(#photoFill)"/>
    </svg>

    <div class="brand">
      <div class="brand-mark"></div>
      <div>
        <div class="brand-name">Brillaria4</div>
        <div class="brand-tagline">Asesoría y administración<br>de empresas</div>
      </div>
    </div>

    <div class="services-title"><span>SERVICIOS</span></div>

    <div class="service" style="left:58px; top:222px;">
      <svg viewBox="0 0 24 24"><rect x="5" y="3" width="14" height="18" rx="1"/><path d="M8 8h8M8 12h8M8 16h5"/></svg>Impuesto
    </div>
    <div class="service" style="left:240px; top:224px;">
      <svg viewBox="0 0 24 24"><rect x="4" y="3" width="16" height="18" rx="1"/><rect x="7" y="6" width="10" height="4"/><path d="M8 14h2M12 14h2M16 14h0M8 17h2M12 17h2"/></svg>Contabilidad
    </div>
    <div class="service" style="left:58px; top:270px;">
      <svg viewBox="0 0 24 24"><circle cx="12" cy="8" r="4"/><path d="M4 21c0-4 4-6 8-6s8 2 8 6"/></svg>Labor
    </div>
    <div class="service" style="left:238px; top:270px;">
      <svg viewBox="0 0 24 24"><circle cx="12" cy="7" r="4"/><path d="M5 21c0-4 3-6 7-6s7 2 7 6"/><rect x="3" y="15" width="7" height="5"/></svg>Administración
    </div>
    <div class="service" style="left:58px; top:313px;">
      <svg viewBox="0 0 24 24"><path d="M9 4h6l-2 4h-2z"/><path d="M11 8c-5 3-7 7-6 10 1 2 4 3 7 3s6-1 7-3c1-3-1-7-6-10"/><path d="M12 12v6M10 14h3a1 1 0 010 2h-2"/></svg>Financiero
    </div>

    <div class="contact-band">
      <div class="contact-call">
        <div class="call-label">Llamanos Estimación gratuita</div>
        <div class="call-number">
          <svg viewBox="0 0 24 24"><path d="M6.6 10.8a15 15 0 006.6 6.6l2.2-2.2a1 1 0 011-.25 11.4 11.4 0 003.6.6 1 1 0 011 1V20a1 1 0 01-1 1A17 17 0 013 4a1 1 0 011-1h3.5a1 1 0 011 1 11.4 11.4 0 00.6 3.6 1 1 0 01-.25 1z"/></svg>600 482 915
        </div>
      </div>
      <div class="contact-divider"></div>
      <div class="contact-online">
        <div class="contact-line">
          <svg viewBox="0 0 24 24"><rect x="3" y="5" width="18" height="14"/><path d="M3 5l9 8 9-8"/></svg>info@brillaria4.com
        </div>
        <div class="contact-line">
          <svg viewBox="0 0 24 24"><circle cx="12" cy="12" r="9"/><path d="M3 12h18M12 3c3 3 3 15 0 18M12 3c-3 3-3 15 0 18"/></svg>www.brillaria4.com
        </div>
      </div>
    </div>
  </section>
</body>
</html>
```